Design a Small Graphic for a client brochure and Website

We need a a fairly simple diagram/graphic to replace the existing graphic in our brochures and website. We are a Private Wealth Advice firm, dealing with high-end clients. We would like to be able to copyright the final design. We need this design to be stylish and have a long shelf-life.
The original design is quite old and was not updated to reflect our company growth or changes in our website design and brochure designs.
Updates

Target Market(s)

Private Wealth clients
High end
Age 45 plus

Industry/Entity Type

Finance

Font styles to use
Sans Serif
Other font styles liked:
• Stag Sans

Requirements
Must have
• Corporate colours only - plus white
• Pantone 288c (Blue)
• Pantone Cool grey 10c
• Pantone 666c (purple - only limited use for highlighting etc)
• Corporate fonts only
• Stag Sans light, book and thin
• Must provide AI editable files
• Must be able to scale to size and remove/replace any text
• Must be in keeping with our brochures and website which can be viewed at www.ridgefold-advisory.com.au
Nice to have
• We want something more vibrant than the image we are using. Something which is in keeping with our image but that is really eye catching.

```html
<!DOCTYPE html>
<html lang="en">
<head>
<meta charset="utf-8">
<title>Your Family – Planning Cycle</title>
<link href="https://fonts.googleapis.com/css2?family=Arimo:wght@700&family=Roboto+Condensed:wght@500&display=swap" rel="stylesheet">
<style>
  :root {
    --blue-light: #5aa0e0;
    --blue: #0a3fc8;
    --blue-deep: #062a8a;
    --grey-light: #b4b8bb;
    --grey: #7b8085;
    --grey-deep: #45494d;
    --lavender-light: #d6d9f6;
    --lavender: #a4abeb;
    --lavender-deep: #555a86;
    --paper: #ffffff;
    --paper-shade: #c9cbcd;
    --ink: #141414;
    --seam: #ffffff;
    --rim: #8e9296;
  }
  html, body {
    margin: 0;
    padding: 0;
    width: 1200px;
    height: 1188px;
    overflow: hidden;
    background: var(--paper);
  }
  .cycle-diagram { display: block; width: 1200px; height: 1188px; }
  .segment { stroke: var(--seam); stroke-width: 6; }
  .segment--legacy { stroke: var(--rim); stroke-width: 3; }
  .connector { stroke: var(--seam); stroke-width: 5; stroke-linejoin: round; }
  .connector--legacy { stroke: var(--rim); stroke-width: 3; }
  .step-number { font-family: "Arimo", Arial, sans-serif; font-weight: 700; font-size: 340px; text-anchor: middle; }
  .step-number--1 { fill: var(--blue-light); opacity: .75; }
  .step-number--2 { fill: var(--grey-light); opacity: .8; }
  .step-number--3 { fill: var(--lavender-light); opacity: .7; }
  .step-number--4 { fill: var(--paper-shade); }
  .step-label { font-family: "Arimo", Arial, sans-serif; font-weight: 700; font-size: 80px; text-anchor: middle; letter-spacing: -2px; fill: var(--ink); }
  .step-label--purpose { fill: var(--paper); }
  .hub { fill: var(--paper); stroke: var(--rim); stroke-width: 3; }
  .hub-label { font-family: "Roboto Condensed", "Arial Narrow", sans-serif; font-weight: 500; font-size: 104px; text-anchor: middle; fill: var(--ink); }
</style>
</head>
<body>
<svg class="cycle-diagram" viewBox="0 0 1200 1188" xmlns="http://www.w3.org/2000/svg" aria-label="Planning cycle centred on your family">
  <defs>
    <radialGradient id="shade-purpose" cx="600" cy="594" r="600" gradientUnits="userSpaceOnUse">
      <stop offset="0.3" stop-color="var(--blue-deep)"/>
      <stop offset="0.55" stop-color="var(--blue)"/>
      <stop offset="1" stop-color="var(--blue-light)"/>
    </radialGradient>
    <radialGradient id="shade-wealth" cx="600" cy="594" r="600" gradientUnits="userSpaceOnUse">
      <stop offset="0.3" stop-color="var(--grey-deep)"/>
      <stop offset="0.6" stop-color="var(--grey)"/>
      <stop offset="1" stop-color="var(--grey-light)"/>
    </radialGradient>
    <linearGradient id="shade-investment" x1="650" y1="650" x2="1150" y2="1150" gradientUnits="userSpaceOnUse">
      <stop offset="0" stop-color="var(--lavender-light)"/>
      <stop offset="0.5" stop-color="var(--lavender)"/>
      <stop offset="1" stop-color="var(--lavender-deep)"/>
    </linearGradient>
    <radialGradient id="shade-legacy" cx="600" cy="594" r="600" gradientUnits="userSpaceOnUse">
      <stop offset="0.3" stop-color="var(--paper-shade)"/>
      <stop offset="0.55" stop-color="var(--paper)"/>
      <stop offset="0.9" stop-color="var(--paper)"/>
      <stop offset="1" stop-color="var(--paper-shade)"/>
    </radialGradient>
    <path id="connector-shape" d="M-12,-27 C14,-27 30,-37 40,-55 L125,0 L40,55 C32,35 14,27 -12,27 Z"/>
  </defs>

  <g class="segments">
    <path class="segment segment--purpose" fill="url(#shade-purpose)" d="M12,594 A588,588 0 0 1 600,6 L600,406 A188,188 0 0 0 412,594 Z"/>
    <path class="segment segment--wealth" fill="url(#shade-wealth)" d="M600,6 A588,588 0 0 1 1188,594 L788,594 A188,188 0 0 0 600,406 Z"/>
    <path class="segment segment--investment" fill="url(#shade-investment)" d="M1188,594 A588,588 0 0 1 600,1182 L600,782 A188,188 0 0 0 788,594 Z"/>
    <path class="segment segment--legacy" fill="url(#shade-legacy)" d="M600,1182 A588,588 0 0 1 12,594 L412,594 A188,188 0 0 0 600,782 Z"/>
  </g>

  <g class="connectors">
    <use href="#connector-shape" class="connector" fill="var(--blue)" transform="translate(598,232)"/>
    <use href="#connector-shape" class="connector" fill="var(--grey)" transform="translate(965,598) rotate(90)"/>
    <use href="#connector-shape" class="connector" fill="var(--lavender)" transform="translate(602,958) rotate(180)"/>
    <use href="#connector-shape" class="connector connector--legacy" fill="var(--paper)" transform="translate(228,602) rotate(-90)"/>
  </g>

  <g class="step-numbers">
    <text class="step-number step-number--1" x="320" y="470">1</text>
    <text class="step-number step-number--2" x="875" y="470">2</text>
    <text class="step-number step-number--3" x="875" y="1030">3</text>
    <text class="step-number step-number--4" x="330" y="1030">4</text>
  </g>

  <g class="step-labels">
    <text class="step-label step-label--purpose" x="365" y="350">Purpose</text>
    <text class="step-label" x="900" y="315">Wealth</text>
    <text class="step-label" x="900" y="395">Planning</text>
    <text class="step-label" x="880" y="850">Investment</text>
    <text class="step-label" x="880" y="930">Planning</text>
    <text class="step-label" x="340" y="840">Your</text>
    <text class="step-label" x="340" y="920">Legacy</text>
  </g>

  <g class="hub-group">
    <circle class="hub" cx="600" cy="594" r="186"/>
    <text class="hub-label" x="603" y="585">YOUR</text>
    <text class="hub-label" x="600" y="685">FAMILY</text>
  </g>
</svg>
</body>
</html>
```